Harrowgate Lending Inc. Investor Presentation

We would like a PowerPoint presentation to attract prospective investors. It needs to look extremely professional since we are a financial lending institution, and seeking capital investors. We specialize in Private Lending with Mortgage Backed Securities, both Residential and Commercial properties.

```html
<!DOCTYPE html>
<html lang="en">
<head>
<meta charset="utf-8">
<title>Harrowgate Lending Inc. Investor Presentation</title>
<link href="https://fonts.googleapis.com/css2?family=Playfair+Display:wght@400;700&family=Lato:wght@300;400&display=swap" rel="stylesheet">
<style>
:root{
  --page:#a9a9a9;
  --dark:#333333;
  --gold:#e4b934;
  --teal:#3aa3ad;
  --cream:#fdf4df;
  --cream-deep:#fbe8bd;
  --white:#ffffff;
  --ink:#333333;
}
*{margin:0;padding:0;box-sizing:border-box}
html,body{width:1200px;height:4283px;overflow:hidden;background:var(--page)}
body{position:relative;font-family:'Lato',sans-serif;color:var(--ink)}
.slide{position:absolute;left:23px;width:1152px;height:648px;overflow:hidden;box-shadow:0 2px 6px rgba(0,0,0,.25);background:var(--white)}
.abs{position:absolute}
.photo{position:absolute}
.title{font-family:'Playfair Display',serif;font-weight:700}
.body-text{font-weight:300;text-align:justify}
.brand{font-family:'Playfair Display',serif;font-weight:400;letter-spacing:1px;line-height:1.1;display:flex;align-items:center;gap:12px}
.brand-mark{width:16px;height:16px;background:var(--gold);flex:none}
.brand-small{position:absolute;font-family:'Playfair Display',serif;font-size:11px;letter-spacing:.5px;color:var(--dark);display:flex;align-items:center;gap:5px}
.brand-small i{display:block;width:9px;height:9px;background:var(--gold)}

/* slide 1 */
.s1{top:75px;background:var(--dark)}
.s1 .band{left:0;top:462px;width:1152px;height:186px;background:var(--gold)}
.s1 .photo{left:60px;top:60px;width:492px;height:588px;background:linear-gradient(135deg,#3b3d44 0%,#5b606b 45%,#c9c9c6 75%,#8a8c8f 100%)}
.s1 .brand{left:690px;top:180px;color:var(--white);font-size:30px}
.s1 .intro{left:661px;top:325px;width:400px;font-size:19px;line-height:30px;color:#eee;font-weight:300}
.social{top:516px;width:74px;height:74px;border-radius:50%;background:var(--dark);color:var(--white);font-size:14px;display:flex;align-items:center;justify-content:center}

/* slide 2 */
.s2{top:766px}
.s2 .band{left:0;top:0;width:352px;height:648px;background:var(--gold)}
.s2 .ph-a{left:43px;top:45px;width:196px;height:281px;background:linear-gradient(180deg,#cfe3f1,#4f7d99 70%,#203a4c)}
.s2 .ph-b{left:43px;top:344px;width:196px;height:256px;background:linear-gradient(180deg,#8fb3cc,#2c4c60 60%,#15242f)}
.s2 .ph-c{left:253px;top:45px;width:197px;height:555px;background:linear-gradient(200deg,#dfeaf3,#6f97b2 40%,#253c4b 80%,#151d24)}
.s2 .head{left:532px;top:126px;height:63px;padding:0 14px;background:var(--dark);color:var(--gold);font-size:31px;letter-spacing:-.3px;display:flex;align-items:center;white-space:nowrap}
.s2 .body-text{left:534px;top:224px;width:508px;font-size:16.5px;line-height:30px}

/* slide 3 */
.s3{top:1456px}
.s3 .head{left:558px;top:108px;font-size:56px;white-space:nowrap}
.s3 .head .gold{color:var(--gold)}
.icon-circle{position:absolute;width:140px;height:140px;border-radius:50%;background:var(--gold);display:flex;align-items:center;justify-content:center}
.s3 .t1{left:599px;top:226px;width:440px;font-size:16px;line-height:30px}
.s3 .t2{left:489px;top:402px;width:430px;font-size:16px;line-height:30px}

/* slide 4 */
.s4{top:2146px}
.s4 .bar{left:0;top:61px;width:60px;height:527px;background:var(--gold)}
.s4 .head{left:98px;top:96px;font-size:34px;line-height:48px;letter-spacing:-.5px;white-space:nowrap}
.s4 .body-text{left:98px;top:228px;width:368px;font-size:19.5px;line-height:36px}
.s4 .ph-a{left:515px;top:61px;width:309px;height:378px;background:linear-gradient(160deg,#b9d3ea,#f1ede6 40%,#c8894a 70%,#555 100%)}
.s4 .ph-b{left:843px;top:61px;width:309px;height:265px;background:linear-gradient(180deg,#dde6ee,#f3f3f1 45%,#a8aca8 70%,#5f8a3f 100%)}
.s4 .accent{left:620px;top:326px;width:37px;height:262px;background:var(--gold)}
.s4 .panel{left:657px;top:326px;width:495px;height:262px;background:var(--dark)}
.s4 .panel p{position:absolute;left:32px;top:43px;width:404px;font-size:19.5px;line-height:36px;color:#eee}

/* slide 5 */
.s5{top:2837px}
.s5 .side{left:765px;top:0;width:387px;height:648px;background:var(--gold)}
.s5 .bar{left:743px;top:60px;width:52px;height:527px;background:var(--dark)}
.s5 .head{left:810px;top:104px;font-size:48px;line-height:52px}
.s5 .body-text{left:810px;top:243px;width:286px;font-size:16px;line-height:30px}
.hub{left:60px;top:204px;width:240px;height:240px;border-radius:50%;background:var(--dark);display:flex;align-items:center;justify-content:center;text-align:center;color:var(--gold);font-family:'Playfair Display',serif;font-size:22px;line-height:1.2}
.bubble{position:absolute;height:55px;border-radius:28px;background:var(--gold);font-size:14px;line-height:19px;padding:8px 0 0 44px;color:var(--dark);font-weight:300}
.bubble::before{content:"";position:absolute;left:-14px;top:18px;border-right:28px solid var(--gold);border-top:9px solid transparent;border-bottom:9px solid transparent}

/* slide 6 */
.s6{top:3527px;background:var(--cream)}
.s6 .topbar{left:494px;top:0;width:658px;height:42px;background:var(--gold);border-bottom-left-radius:14px}
.s6 .strip{left:0;top:63px;width:106px;height:527px;border-radius:0 14px 14px 0;background:linear-gradient(180deg,#6d7c88,#2e3a44 60%,#1d252c)}
.s6 .soft{left:575px;top:462px;width:600px;height:220px;border-radius:40px;background:var(--cream-deep)}
.s6 .brand{left:150px;top:128px;font-size:27px;color:var(--dark)}
.s6 .rule{left:106px;top:283px;width:253px;height:13px;background:var(--gold)}
.contact{position:absolute;left:145px;font-size:20px;display:flex;align-items:center;gap:16px;color:var(--dark)}
.contact svg{width:16px;height:16px}
.diamond{position:absolute;transform:rotate(45deg);border:4px solid var(--white);box-shadow:0 2px 8px rgba(0,0,0,.15)}
</style>
</head>
<body>

<!-- Slide 1: cover -->
<section class="slide s1">
  <div class="abs band"></div>
  <div class="photo" role="img" aria-label="Photo of a businessman pointing a pen at an architectural building model"></div>
  <div class="abs brand"><span class="brand-mark"></span><span>HARROWGATE<br>LENDING</span></div>
  <p class="abs intro">Lorem ipsum dolor sit amet, consectetur adipiscing elit, sed do eiusmod tempor incididunt ut labore et dolore magna aliqua.</p>
  <div class="abs social" style="left:654px">Blog</div>
  <div class="abs social" style="left:752px">Video</div>
  <div class="abs social" style="left:845px">News</div>
  <div class="abs social" style="left:938px">Jobs</div>
</section>

<!-- Slide 2: about -->
<section class="slide s2">
  <div class="abs band"></div>
  <div class="photo ph-a" role="img" aria-label="Glass skyscraper seen from below"></div>
  <div class="photo ph-b" role="img" aria-label="Glass tower facade against the sky"></div>
  <div class="photo ph-c" role="img" aria-label="Tall glass office building looking upward"></div>
  <svg class="abs" style="left:0;top:0" width="1152" height="648">
    <polygon points="887,0 990,0 938,52" fill="var(--gold)"/>
    <polygon points="1152,440 1152,648 1100,648 1028,565" fill="var(--dark)"/>
    <polygon points="1052,512 1102,562 1052,612 1002,562" fill="none" stroke="var(--gold)" stroke-width="3"/>
  </svg>
  <div class="brand-small" style="left:1030px;top:52px"><i></i>HARROWGATE</div>
  <h2 class="abs title head">About Harrowgate Lending Inc.</h2>
  <p class="abs body-text">Lorem ipsum dolor sit amet, consectetur adipiscing elit, sed do eiusmod tempor incididunt ut labore et dolore magna aliqua. Quis ipsum suspendisse ultrices gravida. Risus commodo viverra maecenas accumsan lacus vel facilisis. Lorem ipsum dolor sit amet, consectetur adipiscing elit, sed do eiusmod tempor incididunt ut labore et dolore magna aliqua. Quis ipsum suspendisse ultrices gravida. Risus commodo viverra maecenas accumsan lacus vel facilisis. Lorem ipsum dolor sit amet, consectetur adipiscing elit, sed do eiusmod tempor incididunt ut labore et dolore magna aliqua. Quis ipsum suspendisse ultrices gravida. Risus commodo viverra maecenas accumsan lacus vel facilisis.</p>
</section>

<!-- Slide 3: mission & vision -->
<section class="slide s3">
  <svg class="abs" style="left:0;top:0" width="1152" height="648">
    <polygon points="0,0 326,0 510,648 0,648" fill="var(--gold)"/>
    <polygon points="1074,0 1152,0 1152,190" fill="var(--gold)"/>
    <polygon points="1062,44 1100,82 1062,120 1024,82" fill="var(--gold)"/>
    <polygon points="1062,40 1112,90 1062,140 1012,90" fill="none" stroke="var(--dark)" stroke-width="3"/>
  </svg>
  <svg class="abs" style="left:0;top:0" width="490" height="648" role="img" aria-label="Magnifying glass over miniature paper houses on a teal background">
    <defs><linearGradient id="scene" x1="0" y1="0" x2="0" y2="1"><stop offset="0" stop-color="#3aa3ad"/><stop offset=".55" stop-color="#3aa3ad"/><stop offset=".75" stop-color="#8a7b6c"/><stop offset="1" stop-color="#6b1f1f"/></linearGradient></defs>
    <polygon points="0,0 251,0 487,648 0,648" fill="url(#scene)"/>
  </svg>
  <h2 class="abs title head"><span class="gold">Mission &amp;</span> Vision</h2>
  <div class="icon-circle" style="left:435px;top:214px">
    <svg width="72" height="72" viewBox="0 0 72 72" fill="none" stroke="var(--dark)" stroke-width="4"><circle cx="34" cy="38" r="26"/><circle cx="34" cy="38" r="16"/><circle cx="34" cy="38" r="6"/><path d="M34 38 L60 12 M52 12 H60 V20"/></svg>
  </div>
  <p class="abs body-text t1">Lorem ipsum dolor sit amet, consectetur adipiscing elit, sed do eiusmod tempor incididunt ut labore et dolore magna aliqua. Quis ipsum suspendisse ultrices gravida. Risus commodo viverra maecenas accumsan lacus vel facilisis.</p>
  <p class="abs body-text t2">Lorem ipsum dolor sit amet, consectetur adipiscing elit, sed do eiusmod tempor incididunt ut labore et dolore magna aliqua. Quis ipsum suspendisse ultrices gravida. Risus commodo viverra maecenas accumsan lacus vel facilisis.</p>
  <div class="icon-circle" style="left:954px;top:397px">
    <svg width="80" height="60" viewBox="0 0 80 60" fill="none" stroke="var(--dark)" stroke-width="4"><circle cx="20" cy="40" r="15"/><circle cx="60" cy="40" r="15"/><circle cx="20" cy="40" r="8"/><circle cx="60" cy="40" r="8"/><path d="M8 30 L18 6 H30 L34 26 M72 30 L62 6 H50 L46 26 M34 26 H46"/></svg>
  </div>
  <div class="brand-small" style="left:1030px;top:585px"><i></i>HARROWGATE</div>
</section>

<!-- Slide 4: properties -->
<section class="slide s4">
  <div class="abs bar"></div>
  <h2 class="abs title head">Residential &amp;<br>Commercial properties</h2>
  <p class="abs body-text">Lorem ipsum dolor sit amet, consectetur adipiscing elit, sed do eiusmod tempor incididunt ut labore et dolore magna aliqua. Quis ipsum suspendisse ultrices gravida. Risus commodo viverra maecenas facilisis. Lorem ipsum dolor sit amet, consectetur adipiscing elit, sed do eiusmod tempor incididunt ultrices gravida. Risus commodo viverra maecenas facilisis.</p>
  <div class="photo ph-a" role="img" aria-label="Modern apartment building with balconies"></div>
  <div class="photo ph-b" role="img" aria-label="White residential tower with green lawn"></div>
  <div class="brand-small" style="left:1040px;top:40px"><i></i>HARROWGATE</div>
  <div class="abs accent"></div>
  <div class="abs panel"><p class="body-text">Lorem ipsum dolor sit amet, consectetur adipiscing elit, sed do eiusmod tempor incididunt ut labore et dolore magna aliqua. Quis ipsum suspendisse ultrices gravida. Risus commodo viverra maecenas facilisis.</p></div>
</section>

<!-- Slide 5: overview -->
<section class="slide s5">
  <div class="abs side"></div>
  <div class="abs bar"></div>
  <svg class="abs" style="left:0;top:0" width="700" height="648">
    <path d="M180 118 A206 206 0 0 1 180 530" fill="none" stroke="var(--dark)" stroke-width="5"/>
    <g fill="var(--gold)">
      <circle cx="238" cy="126" r="11"/><circle cx="352" cy="216" r="11"/><circle cx="387" cy="324" r="11"/><circle cx="352" cy="432" r="11"/><circle cx="238" cy="522" r="11"/>
    </g>
  </svg>
  <div class="abs hub">HARROWGATE<br>LENDING</div>
  <div class="bubble" style="left:301px;top:88px;width:282px">Lorem ipsum dolor sit amet, ipsum<br>consectetur adipiscing elit.</div>
  <div class="bubble" style="left:405px;top:191px;width:281px">Lorem ipsum dolor sit amet, ipsum<br>consectetur adipiscing elit.</div>
  <div class="bubble" style="left:434px;top:297px;width:282px">Lorem ipsum dolor sit amet, ipsum<br>consectetur adipiscing elit.</div>
  <div class="bubble" style="left:405px;top:404px;width:284px">Lorem ipsum dolor sit amet, ipsum<br>consectetur adipiscing elit.</div>
  <div class="bubble" style="left:301px;top:507px;width:282px">Lorem ipsum dolor sit amet, ipsum<br>consectetur adipiscing elit.</div>
  <h2 class="abs title head">Harrowgate<br>Lending Inc.</h2>
  <p class="abs body-text">Lorem ipsum dolor sit amet, consectetur adipiscing elit, sed do eiusmod tempor incididunt ut labore et dolore magna aliqua. Quis ipsum suspendisse ultrices gravida. Risus commodo viverra maecenas accumsan lacus. Quis ipsum suspendisse ultrices gravida. Risus commodo viverra maecenas accumsan lacus.</p>
</section>

<!-- Slide 6: contact -->
<section class="slide s6">
  <div class="abs soft"></div>
  <div class="abs topbar"></div>
  <div class="abs strip" role="img" aria-label="Dark glass tower facade"></div>
  <div class="abs brand"><span class="brand-mark"></span><span>HARROWGATE<br>LENDING</span></div>
  <div class="abs rule"></div>
  <div class="contact" style="top:432px"><svg viewBox="0 0 16 16" fill="none" stroke="var(--dark)" stroke-width="1.4"><path d="M3 1.5h3l1.2 3.3-1.8 1.2a8 8 0 0 0 4.6 4.6l1.2-1.8 3.3 1.2v3a1.5 1.5 0 0 1-1.6 1.5A13 13 0 0 1 1.5 3.1 1.5 1.5 0 0 1 3 1.5z"/></svg>+0 555 014 272</div>
  <div class="contact" style="top:476px"><svg viewBox="0 0 16 16" fill="none" stroke="var(--dark)" stroke-width="1.4"><circle cx="8" cy="8" r="6.5"/><path d="M1.5 8h13M8 1.5c-3 3.5-3 9.5 0 13M8 1.5c3 3.5 3 9.5 0 13"/></svg>www.harrowgatelending.com</div>
  <div class="contact" style="top:519px"><svg viewBox="0 0 16 16" fill="none" stroke="var(--dark)" stroke-width="1.4"><rect x="1.5" y="3.5" width="13" height="9"/><path d="M1.5 3.5 8 9l6.5-5.5"/></svg>info@harrowgatelending.com</div>
  <div class="contact" style="top:562px"><svg viewBox="0 0 16 16" fill="var(--dark)"><path d="M8 1a5 5 0 0 0-5 5c0 3.6 5 9 5 9s5-5.4 5-9a5 5 0 0 0-5-5zm0 7a2 2 0 1 1 0-4 2 2 0 0 1 0 4z"/></svg>City, USA</div>
  <div class="diamond" style="left:630px;top:129px;width:200px;height:200px;background:linear-gradient(135deg,#d9a13a,#6b8f3a 50%,#2b3036)" role="img" aria-label="Stacks of coins with a rising growth chart"></div>
  <div class="diamond" style="left:856px;top:119px;width:170px;height:170px;background:linear-gradient(135deg,#3a3d44,#8a6b52 55%,#c9c0b2)" role="img" aria-label="Small model house on a desk with documents"></div>
  <div class="diamond" style="left:738px;top:334px;width:206px;height:206px;background:linear-gradient(135deg,#7d86a0,#3c4766 50%,#1e2438)" role="img" aria-label="Hand using a calculator over financial papers"></div>
</section>

</body>
</html>
```